Proposal Form

Hello! We would like a full color (CMYK) form created with our logo and a similar look and feel to other documents we use (attached). Underneath logo and some design (design should be landscaping based as that is what we will be quoting), we would need a bunch of horizontal lines (for us to write on) and a space in the bottom right which has three lines - (1) Project Total _____________ (2) ______ Monthly Payments of _________________ (3) Pre-pay and receive a 3% discount _______________________

```html
<!DOCTYPE html>
<html lang="en">
<head>
<meta charset="utf-8">
<title>Maple Hollow Landscaping – Proposal Form</title>
<link rel="stylesheet" href="https://fonts.googleapis.com/css2?family=Lato:wght@400;700&display=swap">
<style>
  :root {
    --backdrop: #ececec;
    --paper: #ffffff;
    --ink: #161616;
    --header: #1b1b1c;
    --rule: #c9c9c9;
    --blank-rule: #8a8a8a;
    --band-blue: #3f6f95;
    --footer-text: #f2f2f2;
    --badge-placeholder: #d6d6d6;
  }
  * { margin: 0; padding: 0; box-sizing: border-box; }
  html, body {
    width: 1200px; height: 2253px; overflow: hidden;
    background: var(--backdrop);
    font-family: "Lato", Arial, sans-serif;
    color: var(--ink);
  }
  .proposal-form {
    position: absolute; left: 60px; top: 429px;
    width: 1080px; height: 1394px;
    background: var(--paper);
    box-shadow: 0 3px 10px rgba(0,0,0,0.18);
  }
  .masthead {
    position: absolute; left: 0; top: 0; width: 100%; height: 213px;
    background: var(--header);
  }
  .brand-name {
    position: absolute; left: 0; top: 122px; width: 100%;
    text-align: center; color: #ffffff;
    font-weight: 400; font-size: 32px; letter-spacing: 4px; text-transform: uppercase;
  }
  .garden-banner {
    position: absolute; left: 0; top: 209px; width: 100%; height: 139px;
    background: linear-gradient(90deg, #4d7a2c 0%, #7aa83c 18%, #86b640 40%, #c64f8e 58%, #b53d7d 70%, #5f8b34 85%, #3f6a26 100%);
    border-top: 4px solid var(--band-blue);
  }
  .heading-line {
    position: absolute; left: 301px; top: 456px; width: 477px; height: 2px; background: var(--rule);
  }
  .writing-lines { position: absolute; left: 63px; top: 540px; width: 954px; }
  .writing-lines span {
    display: block; height: 2px; background: var(--rule); margin-bottom: 50.6px;
  }
  .award-badges {
    position: absolute; left: 73px; top: 1152px;
    display: flex; gap: 14px;
  }
  .award-badges .badge {
    width: 92px; height: 118px; border-radius: 10px;
    background: var(--badge-placeholder);
  }
  .totals {
    position: absolute; left: 540px; top: 1142px; width: 477px;
    font-size: 19px; color: var(--ink);
  }
  .totals .row { height: 52px; display: flex; align-items: flex-end; gap: 6px; }
  .totals .blank { flex: 1; height: 1px; background: var(--blank-rule); margin-bottom: 5px; }
  .totals .blank.short { flex: 0 0 118px; }
  .totals .label { white-space: nowrap; line-height: 1; }
  .contact-bar {
    position: absolute; left: 0; bottom: 0; width: 100%; height: 63px;
    background: var(--header); color: var(--footer-text);
    display: flex; align-items: center; justify-content: center; gap: 14px;
    font-size: 16px; font-weight: 700; letter-spacing: 0.5px;
  }
  .contact-bar .divider { width: 28px; height: 2px; background: var(--footer-text); }
</style>
</head>
<body>
  <main class="proposal-form">
    <header class="masthead">
      <div class="brand-name">Maple Hollow Landscaping</div>
    </header>
    <div class="garden-banner" role="img" aria-label="Photo of a landscaped garden lawn with flower beds"></div>

    <div class="heading-line"></div>
    <div class="writing-lines">
      <span></span><span></span><span></span><span></span><span></span><span></span>
      <span></span><span></span><span></span><span></span><span></span>
    </div>

    <div class="award-badges" role="img" aria-label="Service award badges">
      <div class="badge"></div><div class="badge"></div><div class="badge"></div><div class="badge"></div>
    </div>

    <section class="totals">
      <div class="row"><span class="label">Project Total :</span><span class="blank"></span></div>
      <div class="row"><span class="blank short"></span><span class="label">Monthly Payments of:</span><span class="blank"></span></div>
      <div class="row"><span class="label">Pre-pay and receive a 3% discount</span><span class="blank"></span></div>
    </section>

    <footer class="contact-bar">
      <span>CALL US: (555) 014-2270</span>
      <span class="divider"></span>
      <span>hello@maplehollow.com</span>
    </footer>
  </main>
</body>
</html>
```